Law Firm Web Design Project

I need a website design for my law firm. I have attached to this description the URL of a website I liked with a description of the elements of that website that appeal to me.

I am also attaching my law firm's logo, so you can review that design when you create the website design.

Reference Site: www.harbormeadowfamilycounsel.com

What we like about this site:
• The different layers
• Subtle designs, textures, curves
• 3 dimensional
• Floating effect
• Simple logo that stands out (we are providing logo)
• Prominent phone number
• Location of Areas of Practice
oDivorce, Legal Separation, Paternity, Spousal Maintenance, Child Custody, Child Support, Protective Orders, Community Property, Business Evaluations
• The limited amount of links across the top
o Home, Meet Our Attorney, FAQ, Contact Us
• Request A Consultation click through
• Right side bar with the moving icons
• Badges

Other Tips:
• We don’t want the website to be dark. The logo can standout and the website can have its own colors and flow.
• We would like there to be a “call to action” or way to get in touch on every page and every page view
• We would like a place for credit card icons at the bottom of the page
• Strong, yet elegant
• Finally, just use the website provided as a guide. Explore different colors, textures, shapes, shadows etc.
Updates

I would prefer the website have colors that are complementary to my logo and that are strong and elegant.  I like black, gold, amber, and tan colors.  Black should be used sparingly as an accent only, since I don't want the website to be too dark.

Please review the website I provided as an example in my project description.  I really like the three dimensional aspects of that website (web page floating on top of a background and the logo in the upper left floating on top of the web page).  I also like the use of "swirling" on the background and the webpage.  I hope this additional information is helpful.

Requirements
Must have
• I need a place to insert "client testimonials", a place to insert four logos of awards the law firm has received, a place for people to fill out a form to contact the law firm via email, and a place for people to click to review articles I have written.

```html
<!DOCTYPE html>
<html lang="en">
<head>
<meta charset="utf-8">
<title>Ashcombe Law</title>
<link href="https://fonts.googleapis.com/css2?family=Cabin:wght@400;500&family=Noticia+Text:wght@400;700&family=Sorts+Mill+Goudy&display=swap" rel="stylesheet">
<style>
:root{
  --curtain:#c4672a;
  --curtain-dark:#9c4a1a;
  --cream:#ece4cf;
  --cream-light:#f3ecdb;
  --tan:#d9c197;
  --gold:#a29a55;
  --ink:#3a3a3a;
  --charcoal:#363636;
  --text:#5c4c3c;
  --body:#5a5045;
  --accent:#d2733b;
  --heading:#8a7255;
  --blue:#3c5aa0;
}
*{margin:0;padding:0;box-sizing:border-box}
html,body{width:1044px;height:1200px;overflow:hidden}
body{position:relative;background:linear-gradient(90deg,var(--curtain-dark) 0,var(--curtain) 4%,#d57a3a 6%,var(--curtain) 8%,var(--curtain-dark) 9%,var(--curtain) 91%,var(--curtain-dark) 92%,#d57a3a 95%,var(--curtain) 97%,var(--curtain-dark) 100%);font-family:'Cabin',sans-serif}
.page{position:absolute;left:93px;top:0;width:854px;height:1200px;background:var(--cream);box-shadow:0 0 12px rgba(0,0,0,.45)}
.header{position:absolute;left:0;top:0;width:854px;height:125px;background:linear-gradient(90deg,#efe9d8 0,#ece4cf 50%,#f2ebd9 100%)}
.header-sweep{position:absolute;right:0;top:0;width:470px;height:93px;background:linear-gradient(180deg,#f5efde,#e6dcc2);border-bottom-left-radius:60px 90px}
.brand{position:absolute;left:14px;top:30px;display:flex;align-items:center;gap:18px}
.brand-mark{width:58px;height:58px;background:var(--ink)}
.brand-name{font-family:'Sorts Mill Goudy',serif;font-size:44px;color:var(--gold);line-height:1}
.call{position:absolute;left:502px;top:35px;color:var(--accent);font-size:15px}
.call b{font-weight:400;color:var(--ink);font-size:29px;margin-left:4px;vertical-align:-3px}
.nav{position:absolute;left:392px;top:91px;width:462px;height:34px;background:var(--ink);border-top:3px solid var(--accent);border-top-left-radius:34px 32px;display:flex;align-items:center;justify-content:flex-end;padding-right:12px}
.nav a{color:#fff;text-decoration:none;font-size:14px;padding:0 14px;border-left:1px solid #777;line-height:16px}
.nav a:first-child{border-left:0;color:#d9b45a}
.hero{position:absolute;left:0;top:125px;width:854px;height:263px;background:linear-gradient(100deg,#c9a983 0,#d8c3a4 35%,#8f9a88 60%,#6f8a82 80%,#a48d70 100%)}
.dots{position:absolute;left:46px;top:240px;display:flex;gap:4px}
.dots span{width:14px;height:14px;border-radius:50%;background:#fff}
.dots span:first-child{background:var(--accent)}
.consult{position:absolute;left:662px;top:206px;width:202px;height:45px;background:var(--cream-light);border-radius:14px 4px 14px 4px;box-shadow:0 2px 5px rgba(0,0,0,.35);font-family:'Noticia Text',serif;font-weight:700;font-size:21px;color:var(--ink);display:flex;align-items:center;justify-content:center}
.hero-rule{position:absolute;left:0;top:388px;width:854px;height:3px;background:#4a4a4a}
.side-head{position:absolute;height:29px;background:var(--ink);color:#fff;font-size:13px;display:flex;align-items:flex-end;padding-bottom:5px;border-top-right-radius:6px;border-top-left-radius:6px}
.left-col{position:absolute;left:0;top:391px;width:209px;height:609px;border-right:1px solid #c7b48f;background:var(--tan)}
.left-col .side-head{left:0;width:209px;justify-content:center;border-top-left-radius:0}
.practice{position:absolute;left:40px;top:58px;list-style:none}
.practice li{font-size:12.5px;color:var(--text);height:24.4px}
.qc-text{position:absolute;left:40px;top:345px;font-size:9px;color:var(--text);line-height:14.5px;width:150px}
.field{position:absolute;left:39px;width:134px;height:19px;background:#fff;border-radius:3px;font-size:9px;color:#777;padding:4px 10px}
.submit{position:absolute;left:106px;top:544px;width:67px;height:19px;background:var(--blue);border-radius:3px;color:#fff;font-size:11px;font-weight:500;text-align:center;line-height:19px}
.main{position:absolute;left:209px;top:395px;width:438px;height:605px;background:var(--tan);border-top-right-radius:50px;box-shadow:3px 0 4px rgba(0,0,0,.18)}
.main h1{position:absolute;left:53px;top:28px;font-family:'Noticia Text',serif;font-weight:400;font-size:24px;color:var(--heading)}
.copy{position:absolute;left:53px;top:68px;width:370px;white-space:nowrap;font-family:'Noticia Text',serif;font-size:11px;line-height:20px;color:var(--body);letter-spacing:.2px}
.copy p{margin-bottom:20px}
.copy ul{list-style:none;margin-bottom:20px}
.copy li{padding-left:18px;position:relative}
.copy li:before{content:"";position:absolute;left:2px;top:7px;width:7px;height:7px;border-radius:50%;background:#6a6258}
.divider{position:absolute;left:72px;top:466px;width:335px;height:1px;background:#b39c74}
.badge{position:absolute;background:#c8b188;border-radius:3px}
.right-col{position:absolute;left:668px;top:391px;width:186px;height:609px;background:var(--cream)}
.right-col .side-head{left:0;width:186px;justify-content:center;border-top-right-radius:0}
.box-icon{position:absolute;left:23px;width:38px;height:50px;background:#b8a98c;border-radius:5px}
.box-text{position:absolute;left:72px;width:100px;font-family:'Noticia Text',serif;font-size:9px;line-height:14px;color:var(--body)}
.box-text a{display:block;margin-top:6px;color:var(--accent);text-decoration:none}
.box-rule{position:absolute;left:18px;width:168px;height:1px;background:#c8b898}
.footer{position:absolute;left:0;top:1000px;width:854px;height:200px;background:var(--charcoal)}
.f-links{position:absolute;left:91px;top:30px;font-size:8.5px;color:#ddd}
.f-text{position:absolute;left:91px;top:52px;width:450px;font-family:'Noticia Text',serif;font-size:9.3px;line-height:13px;color:#e8d9b0}
.f-rule{position:absolute;left:0;top:94px;width:854px;height:1px;background:#555}
.f-copy{position:absolute;left:91px;top:113px;font-size:8.5px;color:#ddd}
.accept{position:absolute;left:380px;top:115px;font-family:'Noticia Text',serif;font-weight:700;font-size:10px;color:#bbb}
.cards{position:absolute;left:348px;top:132px;display:flex;gap:2px}
.cards span{width:39px;height:25px;background:#c9c9c9}
.f-brand{position:absolute;left:587px;top:34px;display:flex;align-items:center;gap:10px}
.f-brand .brand-mark{width:30px;height:30px;background:#111}
.f-brand .brand-name{font-size:23px}
.f-phone{position:absolute;left:638px;top:70px;font-size:21px;color:#fff}
.f-addr{position:absolute;left:640px;top:97px;width:140px;text-align:center;font-family:'Noticia Text',serif;font-size:8px;line-height:11px;color:#eee}
</style>
</head>
<body>
<div class="page">
  <header class="header">
    <div class="header-sweep"></div>
    <div class="brand"><span class="brand-mark"></span><span class="brand-name">Ashcombe Law</span></div>
    <div class="call">Call Today: <b>555.018.2040</b></div>
    <nav class="nav"><a>Home</a><a>Meet our Attorneys</a><a>Resources</a><a>FAQ</a><a>Contact</a></nav>
  </header>

  <section class="hero" role="img" aria-label="Photo of a smiling family walking barefoot along a sandy beach by the sea">
    <div class="dots"><span></span><span></span><span></span><span></span></div>
    <div class="consult">Consult Us Now!</div>
  </section>
  <div class="hero-rule"></div>

  <aside class="left-col">
    <div class="side-head" style="top:20px">AREAS OF PRACTICE</div>
    <ul class="practice">
      <li>Divorce</li><li>Legal Separation</li><li>Paternity</li><li>Spousal Maintenance</li><li>Child Custody</li><li>Child Support</li><li>Protective Orders</li><li>Community Property</li><li>Business Evaluations</li>
    </ul>
    <div class="side-head" style="top:301px">QUICK CONTACT</div>
    <p class="qc-text">Aliquam congue fermentum nisl. Mauris accumsan nulla vel diam.</p>
    <div class="field" style="top:376px">Name</div>
    <div class="field" style="top:399px">Phone</div>
    <div class="field" style="top:422px">Email</div>
    <div class="field" style="top:445px;height:89px">About your case...</div>
    <div class="submit">Submit</div>
  </aside>

  <main class="main">
    <h1>Welcome to Ashcombe</h1>
    <div class="copy">
      <p>Aliquam congue fermentum nisl. Mauris accumsan nulla<br>vel diam. Sed in lacus ut enim adipiscing aliquet.</p>
      <p>Nulla venenatis. In pede mi, aliquet sit amet, euismod in,<br>auctor ut, ligula. Aliquam dapibus tincidunt metus. Praesent<br>justo dolor, lobortis quis, lobortis dignissim, pulvinar ac,<br>lorem. Vestibulum sed ante. Donec sagittis euismod purus.</p>
      <ul><li>Praesent justo dolor</li><li>Donec sagittis euismod purus</li><li>Mauris accumsan nulla vel diam</li></ul>
      <p>Aliquam congue fermentum nisl. Mauris accumsan nulla<br>vel diam. Sed in lacus ut enim adipiscing aliquet.</p>
      <p>Nulla venenatis. In pede mi, aliquet sit amet, euismod in,<br>auctor ut, ligula. Aliquam dapibus tincidunt metus. Praesent<br>justo dolor, lobortis quis, lobortis dignissim, pulvinar ac,<br>lorem. Vestibulum sed ante. Donec sagittis euismod purus.</p>
    </div>
    <div class="divider"></div>
    <div class="badge" style="left:66px;top:502px;width:100px;height:62px"></div>
    <div class="badge" style="left:192px;top:502px;width:40px;height:62px"></div>
    <div class="badge" style="left:262px;top:502px;width:128px;height:62px"></div>
  </main>

  <aside class="right-col">
    <div class="side-head" style="top:20px">CLICK TO CALL</div>
    <div class="box-icon" style="top:65px;width:30px;left:27px"></div>
    <div class="box-text" style="top:64px">Aliquam congue fermentum nisl. Mauris accumsan nulla vel diam.<a>Click here &gt;&gt;</a></div>
    <div class="box-rule" style="top:153px"></div>

    <div class="side-head" style="top:164px">AWARDS</div>
    <div class="box-icon" style="top:208px"></div>
    <div class="box-text" style="top:203px">Aliquam congue fermentum nisl. Mauris accumsan nulla vel diam.<a>Click here &gt;&gt;</a></div>
    <div class="box-rule" style="top:288px"></div>

    <div class="side-head" style="top:301px">TESTIMONIALS</div>
    <div class="box-icon" style="top:345px"></div>
    <div class="box-text" style="top:339px">Aliquam congue fermentum nisl. Mauris accumsan nulla vel diam.<a>Click here &gt;&gt;</a></div>
    <div class="box-rule" style="top:426px"></div>

    <div class="side-head" style="top:442px">CASE EVALUATION</div>
    <div class="box-icon" style="top:486px"></div>
    <div class="box-text" style="top:481px">Aliquam congue fermentum nisl. Mauris accumsan nulla vel diam.<a>Click here &gt;&gt;</a></div>
    <div class="box-rule" style="top:577px"></div>
  </aside>

  <footer class="footer">
    <div class="f-links">Ashcombe Law &nbsp;|&nbsp; Contact Us &nbsp;|&nbsp; Resources &nbsp;|&nbsp; Privacy Policy &nbsp;|&nbsp; Site Map</div>
    <p class="f-text">Aliquam congue fermentum nisl. Mauris accumsan nulla vel diam. Sed in lacus ut enim adipiscing aliquet. Praesent justo dolor, lobortis quis, lobortis dignissim, pulvinar ac, lorem.</p>
    <div class="f-rule"></div>
    <div class="f-copy">Copyright © 2012. &nbsp;Ashcombe Law. &nbsp;All Rights Reserved.</div>
    <div class="accept">We proudly accept</div>
    <div class="cards"><span></span><span></span><span></span><span></span></div>
    <div class="f-brand"><span class="brand-mark"></span><span class="brand-name">Ashcombe Law</span></div>
    <div class="f-phone">555.018.2040</div>
    <div class="f-addr">48 Linden Row, Suite 310<br>Fairhaven, Ohio 4417</div>
  </footer>
</div>
</body>
</html>
```